Business Card Design

Name of company: Brisk Estate Maintenance.
We are a new start up business.
The company is involved in general property maintenance around residential properties and high rise apartment buildings.
We carry out all types of property maintenance such as:
*Handyman work
*Plumbing
*Painting
*Electrical
*Window cleaning
*Gardens / Landscaping

Target Market(s)

*Real Estate Agents
*Body corporate managers
*Private apartment owners

Industry/Entity Type

Property Maintenance

Requirements
Must have
• Name: Colin Marsh
Address: PO Box 3826
Westmere Crossing
NSW 2117
Phone: 0498 306 259
Email: colin@briskestatemaintenance
Website: www.briskestatemaintenance.com.au
Nice to have
• We don't have any corporate logo so you can design what you think is appropriate

```html
<!DOCTYPE html>
<html lang="en">
<head>
<meta charset="utf-8">
<title>Brisk Estate Maintenance – Business Card</title>
<link rel="stylesheet" href="https://fonts.googleapis.com/css2?family=Jost:wght@300;400;600&display=swap">
<style>
  :root {
    --gold: #a88a3a;
    --ink: #1b1b1b;
    --card-black: #222222;
    --paper: #ffffff;
    --muted: #6a6a6a;
    --stage: #e9e8e5;
  }
  * { margin: 0; padding: 0; box-sizing: border-box; }
  html, body {
    width: 1200px; height: 720px; overflow: hidden;
    background: var(--stage);
    font-family: "Jost", sans-serif;
  }
  .canvas {
    position: relative; width: 1200px; height: 720px;
    display: flex; align-items: center; justify-content: center; gap: 50px;
  }
  .card {
    position: relative; width: 525px; height: 300px; overflow: hidden;
    box-shadow: 0 10px 28px rgba(0,0,0,.18);
  }
  .brand {
    display: flex; align-items: center; gap: 10px;
  }
  .brand__mark {
    width: 12px; height: 12px; background: var(--gold); flex: none;
  }
  .brand__name {
    color: var(--gold); font-weight: 400; letter-spacing: .04em; white-space: nowrap;
  }

  /* Front */
  .card--front { background: var(--paper); color: var(--ink); }
  .card__swoosh { position: absolute; inset: 0; width: 100%; height: 100%; }
  .card--front .brand { position: absolute; left: 34px; top: 26px; }
  .card--front .brand__name { font-size: 20px; }
  .contact { position: absolute; left: 34px; top: 70px; }
  .contact__name { color: var(--gold); font-weight: 600; font-size: 22px; line-height: 1.15; }
  .contact__role { color: var(--muted); font-weight: 300; font-size: 13px; margin-bottom: 8px; }
  .contact__line { font-size: 12.5px; font-weight: 300; line-height: 1.6; }
  .contact__line b { font-weight: 600; }
  .contact__web { font-size: 12.5px; font-weight: 600; margin-top: 3px; }
  .address {
    position: absolute; right: 44px; top: 104px;
    font-size: 14px; font-weight: 600; font-style: normal; line-height: 1.45;
  }

  /* Back */
  .card--back {
    background: var(--card-black);
    display: flex; align-items: center; justify-content: center;
  }
  .card--back .brand__name { font-size: 30px; }
  .card--back .brand__mark { width: 16px; height: 16px; }
</style>
</head>
<body>
<main class="canvas">
  <section class="card card--front" aria-label="Business card front">
    <svg class="card__swoosh" viewBox="0 0 525 300" preserveAspectRatio="none" aria-hidden="true">
      <path d="M0 300 L0 236 C140 250 330 252 440 222 C485 210 510 196 525 180 L525 300 Z" fill="var(--ink)"/>
      <path d="M0 300 L0 262 C150 262 330 262 445 234 C488 223 512 210 525 198 L525 300 Z" fill="var(--paper)"/>
      <path d="M0 300 L0 270 C160 270 340 270 452 242 C492 232 514 220 525 209 L525 300 Z" fill="var(--gold)"/>
    </svg>
    <div class="brand">
      <span class="brand__mark" aria-hidden="true"></span>
      <span class="brand__name">Brisk Estate Maintenance</span>
    </div>
    <div class="contact">
      <div class="contact__name">Colin Marsh</div>
      <div class="contact__role">Owner</div>
      <div class="contact__line"><b>Phone:</b> 0498 306 259</div>
      <div class="contact__line"><b>Email:</b> colin@briskestatemaintenance</div>
      <div class="contact__web">www.briskestatemaintenance.com.au</div>
    </div>
    <address class="address">
      PO Box 3826<br>Westmere Crossing<br>NSW 2117
    </address>
  </section>

  <section class="card card--back" aria-label="Business card back">
    <div class="brand">
      <span class="brand__mark" aria-hidden="true"></span>
      <span class="brand__name">Brisk Estate Maintenance</span>
    </div>
  </section>
</main>
</body>
</html>
```